Business Card Design

I need a business card for my corporation. We are a fast food Mexican Taqueria located in San Jose, CA. I want the cards to include our business logo. The cards need to be simple but elegant. Our theme through out our locations is a beach feel atmosphere. I would like to see cards with a beach feeling. Our website is tacoslapalmera.net and it would be great if the cards matched our website.

Industry/Entity Type

Business

Contact Information for Business Card

Marisol Fuentes, VP
2417 Cedar Brook Ave
San Jose, CA 95482
Direct: 4087326159

```html
<!DOCTYPE html>
<html lang="en">
<head>
<meta charset="utf-8">
<title>La Palmera — Business Card</title>
<link rel="stylesheet" href="https://fonts.googleapis.com/css2?family=Arimo:wght@700&family=Tinos:wght@400;700&display=swap">
<style>
  :root {
    --backdrop: #8c8c8c;
    --card-white: #f7f6f3;
    --brand-red: #b3212b;
    --ink: #1a1a1a;
    --sky-top: #4f9fd4;
    --sky-low: #9cc7e0;
    --sunset: #f2a33a;
    --sea: #2f8ea0;
    --sea-deep: #1f6f82;
    --wood-light: #9a6a3f;
    --wood-dark: #5e3c20;
    --sign-paper: #ece3cf;
    --sand: #e9e2d2;
    --foam: #ffffff;
  }
  * { box-sizing: border-box; margin: 0; padding: 0; }
  html, body { width: 1200px; height: 686px; overflow: hidden; }
  body {
    background: var(--backdrop);
    display: flex;
    align-items: center;
    justify-content: center;
    gap: 40px;
  }
  .card {
    position: relative;
    width: 540px;
    height: 309px;
    overflow: hidden;
    box-shadow: 0 6px 18px rgba(0,0,0,.25);
  }

  /* Front side */
  .front-photo {
    position: absolute; inset: 0;
    background: linear-gradient(180deg,
      var(--sky-top) 0%, var(--sky-low) 28%, var(--sunset) 40%,
      var(--sea) 44%, var(--sea-deep) 62%, var(--wood-light) 66%, var(--wood-dark) 100%);
  }
  .front-badge {
    position: absolute;
    left: 60px; top: 28px;
    width: 300px; height: 140px;
    border-radius: 50%;
    background: var(--card-white);
    display: flex; align-items: center; justify-content: center;
  }
  .brand-name {
    font-family: "Tinos", serif;
    font-weight: 400;
    color: var(--brand-red);
    line-height: 1;
    white-space: nowrap;
  }
  .front-badge .brand-name { font-size: 54px; }
  .front-website {
    position: absolute;
    left: 90px; bottom: 58px;
    font-family: "Tinos", serif;
    font-weight: 700;
    font-size: 24px;
    color: #ffffff;
    letter-spacing: .5px;
  }

  /* Back side */
  .back { background: var(--card-white); }
  .back-photo {
    position: absolute;
    right: 0; top: 0;
    width: 300px; height: 231px;
    background: linear-gradient(180deg,
      var(--sky-top) 0%, var(--foam) 30%, var(--sea) 50%, var(--foam) 72%, var(--sand) 100%);
    -webkit-mask-image: linear-gradient(90deg, transparent 0%, #000 25%);
            mask-image: linear-gradient(90deg, transparent 0%, #000 25%);
  }
  .back-wood {
    position: absolute;
    left: 0; bottom: 0;
    width: 540px; height: 78px;
    background: linear-gradient(180deg, var(--wood-light), var(--wood-dark));
  }
  .back-logo {
    position: absolute;
    left: 44px; top: 100px;
  }
  .back-logo .brand-name { font-size: 38px; }
  .sign {
    position: absolute;
    left: 262px; top: 50px;
    width: 246px; height: 160px;
    background: var(--sign-paper);
    transform: rotate(4deg);
  }
  .sign-text {
    position: absolute;
    left: 280px; top: 78px;
    width: 220px;
    transform: rotate(4deg);
    transform-origin: left top;
  }
  .sign-name {
    font-family: "Arimo", sans-serif;
    font-weight: 700;
    font-size: 21px;
    color: var(--ink);
  }
  .sign-title {
    font-family: "Arimo", sans-serif;
    font-weight: 700;
    font-size: 12px;
    color: var(--ink);
    margin-bottom: 6px;
  }
  .sign-address {
    font-family: "Tinos", serif;
    font-size: 14px;
    line-height: 1.3;
    color: var(--ink);
  }
</style>
</head>
<body>
  <section class="card front">
    <div class="front-photo" role="img" aria-label="Beach photograph at sunset with sea and a wooden boardwalk in the foreground"></div>
    <div class="front-badge"><span class="brand-name">La Palmera</span></div>
    <p class="front-website">tacoslapalmera.net</p>
  </section>

  <section class="card back">
    <div class="back-photo" role="img" aria-label="Beach photograph with turquoise sea, breaking waves and sand"></div>
    <div class="back-wood" role="img" aria-label="Weathered wooden planks"></div>
    <div class="back-logo"><span class="brand-name">La Palmera</span></div>
    <div class="sign" role="img" aria-label="Wooden beach signboard illustration"></div>
    <div class="sign-text">
      <p class="sign-name">Marisol Fuentes</p>
      <p class="sign-title">VP</p>
      <p class="sign-address">2417 Cedar Brook Ave San Jose<br>CA 95482 Direct: 4087326159</p>
    </div>
  </section>
</body>
</html>
```